Sun Path & Clear Way
Use same font as used in my logo
Marla Tenbeck
48207 hwy 19 north dalworth, ar 71482
mltenbeck@mailvox.example
Please change the color of the logo. i will send the color code. Also need changes to letterhead, envelope & card. need asap. thanks.

```html
<!DOCTYPE html>
<html lang="en">
<head>
<meta charset="utf-8">
<title>Sun Path &amp; Clear Way — Stationery Set</title>
<link rel="stylesheet" href="https://fonts.googleapis.com/css2?family=Caveat:wght@500&family=Questrial&display=swap">
<style>
  :root {
    --peach: #f6a37c;
    --peach-text: #ef9a72;
    --ink: #1e1e1e;
    --grey-text: #6d6d6d;
    --paper: #ffffff;
    --stage: #ffffff;
    --edge: #d9d9d9;
    --ghost: #efeff1;
  }
  * { box-sizing: border-box; margin: 0; padding: 0; }
  html, body { width: 1200px; height: 794px; overflow: hidden; background: var(--stage); }
  body { position: relative; font-family: "Questrial", sans-serif; color: var(--grey-text); }

  .sheet { position: absolute; background: var(--paper); border: 1px solid var(--edge); overflow: hidden; }
  .wave { position: absolute; left: 0; top: 0; width: 100%; display: block; }

  .brand { position: absolute; display: flex; align-items: center; gap: 8px; }
  .brand-dot { border-radius: 50%; background: var(--peach); flex: none; }
  .brand-name { font-family: "Caveat", cursive; font-weight: 500; color: var(--ink); line-height: 1; white-space: nowrap; }
  .brand-tagline { position: absolute; color: var(--peach-text); letter-spacing: 0.25em; text-transform: uppercase; white-space: nowrap; }

  /* Letterhead */
  .letterhead { left: 65px; top: 29px; width: 446px; height: 739px; }
  .letterhead .wave { height: 90px; }
  .letterhead .brand { left: 40px; top: 66px; }
  .letterhead .brand-dot { width: 34px; height: 34px; }
  .letterhead .brand-name { font-size: 24px; }
  .letterhead .brand-tagline { left: 42px; top: 106px; font-size: 7px; }
  .letterhead .watermark { position: absolute; left: 100px; top: 262px; width: 246px; height: 246px; border-radius: 50%; background: var(--ghost); }
  .letterhead .footer { position: absolute; left: 28px; bottom: 20px; font-size: 6.5px; white-space: nowrap; }

  /* Business card */
  .card { left: 600px; top: 168px; width: 257px; height: 125px; }
  .card .wave { height: 38px; }
  .card .brand { left: 14px; top: 22px; gap: 5px; }
  .card .brand-dot { width: 18px; height: 18px; }
  .card .brand-name { font-size: 12px; }
  .card .brand-tagline { left: 15px; top: 44px; font-size: 4px; }
  .card .person { position: absolute; left: 150px; top: 30px; }
  .card .person-name { color: var(--peach-text); font-size: 8px; }
  .card .person-role { font-size: 4.5px; margin-top: 1px; }
  .card .slogan { position: absolute; left: 18px; top: 58px; font-family: "Caveat", cursive; font-weight: 500; font-size: 10px; color: var(--peach-text); }
  .card .contact { position: absolute; left: 170px; top: 74px; font-size: 5px; line-height: 1.55; }
  .card .status { position: absolute; left: 60px; bottom: 8px; font-size: 4.5px; }

  /* Envelope */
  .envelope { left: 617px; top: 336px; width: 530px; height: 252px; }
  .envelope .wave { height: 64px; }
  .envelope .brand { left: 14px; top: 84px; }
  .envelope .brand-dot { width: 30px; height: 30px; }
  .envelope .brand-name { font-size: 21px; }
  .envelope .brand-tagline { left: 16px; top: 120px; font-size: 6px; }
  .envelope .return { position: absolute; left: 16px; top: 134px; font-size: 5px; }
  .envelope .badge { position: absolute; left: 362px; top: 112px; width: 96px; height: 96px; border-radius: 50%; background: var(--peach); display: flex; align-items: center; justify-content: center; text-align: center; font-family: "Caveat", cursive; font-weight: 500; font-size: 15px; line-height: 1.05; color: var(--ink); padding: 10px; }
</style>
</head>
<body>

<section class="sheet letterhead" aria-label="Letterhead">
  <svg class="wave" viewBox="0 0 446 90" preserveAspectRatio="none" aria-hidden="true">
    <path d="M0 0 H446 V38 C380 20 320 28 250 48 C170 70 90 76 0 58 Z" fill="var(--peach)"/>
    <path d="M0 60 C90 78 170 72 250 50 C320 30 380 22 446 40" fill="none" stroke="var(--ink)" stroke-width="2"/>
  </svg>
  <div class="brand"><span class="brand-dot"></span><span class="brand-name">Sun Path &amp; Clear Way</span></div>
  <div class="brand-tagline">Feeding our neighbors</div>
  <div class="watermark" aria-hidden="true"></div>
  <p class="footer">48207 hwy 19 north dalworth, ar 71482 &nbsp;|&nbsp; 479-555-0142 &nbsp;|&nbsp; mltenbeck@mailvox.example</p>
</section>

<section class="sheet card" aria-label="Business card">
  <svg class="wave" viewBox="0 0 257 38" preserveAspectRatio="none" aria-hidden="true">
    <path d="M0 0 H257 V14 C215 6 180 10 140 20 C90 32 45 34 0 26 Z" fill="var(--peach)"/>
    <path d="M0 27 C45 35 90 33 140 21 C180 11 215 7 257 15" fill="none" stroke="var(--ink)" stroke-width="1.2"/>
  </svg>
  <div class="brand"><span class="brand-dot"></span><span class="brand-name">Sun Path &amp; Clear Way</span></div>
  <div class="brand-tagline">Feeding our neighbors</div>
  <div class="person">
    <p class="person-name">Marla Tenbeck</p>
    <p class="person-role">founder</p>
  </div>
  <p class="slogan">providing food for the hungry</p>
  <p class="contact">48207 hwy<br>19 north dalworth,<br>ar 71482<br>479-555-0142<br>mltenbeck@mailvox.example</p>
  <p class="status">a non profit 501c3</p>
</section>

<section class="sheet envelope" aria-label="Envelope">
  <svg class="wave" viewBox="0 0 530 64" preserveAspectRatio="none" aria-hidden="true">
    <path d="M0 0 H530 V26 C450 12 380 16 300 30 C200 48 100 50 0 38 Z" fill="var(--peach)"/>
    <path d="M0 39 C100 51 200 49 300 31 C380 17 450 13 530 27" fill="none" stroke="var(--ink)" stroke-width="1.8"/>
  </svg>
  <div class="brand"><span class="brand-dot"></span><span class="brand-name">Sun Path &amp; Clear Way</span></div>
  <div class="brand-tagline">Feeding our neighbors</div>
  <p class="return">48207 hwy 19 north dalworth, ar 71482</p>
  <div class="badge">providing food for the hungry</div>
</section>

</body>
</html>
```